FSG Brochure

We have a compliance document called a Financial Services Guide (FSG) that must be provided to each of our clients either digitally or as a printed document. Attached is the content we require and a rough idea of how we want it laid out - although we are not committed to any of the layout/colours that are in that draft - that is just how the document was pulled together.. I have also included our existing FSG document which we will be replacing, and some variations on our company logo.

```html
<!DOCTYPE html>
<html lang="en">
<head>
<meta charset="utf-8">
<title>Financial Service Guide – pages 4 and 5</title>
<link rel="stylesheet" href="https://fonts.googleapis.com/css2?family=Montserrat:wght@400;500;700&display=swap">
<style>
  :root {
    --navy-bg: #13225e;
    --ink: #1f2a5a;
    --orange: #f28a1d;
    --paper: #ffffff;
    --photo-warm: #b7834c;
    --photo-dark: #3a3230;
  }
  * { margin: 0; padding: 0; box-sizing: border-box; }
  html, body { width: 1200px; height: 1000px; overflow: hidden; }
  body {
    background: var(--navy-bg);
    font-family: "Montserrat", sans-serif;
    color: var(--ink);
    position: relative;
  }
  .spread {
    position: absolute; left: 99px; top: 146px;
    width: 1002px; height: 708px; background: var(--paper);
    overflow: hidden;
  }
  .brand {
    position: absolute; top: 32px;
    display: flex; align-items: center; gap: 5px;
    font-size: 8.5px; font-weight: 700; color: var(--ink); line-height: 10px;
  }
  .brand-dot { width: 8px; height: 8px; border-radius: 50%; background: var(--orange); }
  .brand--left { left: 30px; }
  .brand--right { right: 32px; }
  .header-rule {
    position: absolute; left: 114px; top: 34px;
    width: 774px; height: 5px; background: var(--orange);
  }
  .column {
    position: absolute; font-size: 9.3px; line-height: 17px; white-space: nowrap;
  }
  .col-a { left: 30px; top: 69px; width: 218px; }
  .col-b { left: 255px; top: 69px; width: 212px; }
  .col-c { left: 531px; top: 68px; width: 252px; }
  .col-d { left: 788px; top: 68px; width: 190px; line-height: 16.8px; }
  .subhead { font-size: 10.5px; font-weight: 700; margin-top: 16px; line-height: 17px; }
  .section-title {
    display: flex; align-items: center; gap: 6px;
    font-size: 11.5px; font-weight: 700; line-height: 17px;
  }
  .col-c .section-title { margin-bottom: 9px; }
  .section-num {
    display: inline-flex; align-items: center; justify-content: center;
    width: 14px; height: 14px; background: var(--orange); color: var(--paper);
    font-size: 10px;
  }
  .col-c p { margin-bottom: 8px; }
  strong, .bold { font-weight: 700; }
  .photo {
    position: absolute; left: 272px; top: 354px; width: 186px; height: 278px;
    background: linear-gradient(160deg, var(--photo-warm) 0%, #8a6a55 45%, var(--photo-dark) 100%);
  }
  .instruction {
    position: absolute; left: 531px; top: 564px; width: 450px;
    font-size: 8.8px; line-height: 17px; font-weight: 700; white-space: nowrap;
  }
  .instruction h3 { font-size: 10.5px; font-weight: 700; }
  .footer-label {
    position: absolute; top: 668px;
    font-size: 7px; font-weight: 700; color: var(--orange); letter-spacing: .2px;
  }
  .footer-label--left { left: 30px; }
  .footer-label--right { right: 31px; }
  .page-num {
    position: absolute; top: 883px; color: var(--paper); font-size: 13px;
  }
  .page-num--left { left: 99px; }
  .page-num--right { right: 99px; }
</style>
</head>
<body>
  <section class="spread">
    <div class="brand brand--left"><span class="brand-dot"></span>Hollowbrook</div>
    <div class="header-rule"></div>
    <div class="brand brand--right"><span class="brand-dot"></span>Hollowbrook</div>

    <div class="column col-a">
      <p>superannuation, or investment product issuers.<br>Where the recommendations include the<br>purchase of a new financial product your<br>Adviser will work with you to complete the<br>relevant <strong>Product Application Form</strong>. This may<br>be online or paper based.</p>
      <h3 class="subhead">General advice</h3>
      <p>Your Adviser may provide you with general<br>advice that does not consider your personal<br>circumstances, needs or objectives. Your<br>Adviser will give you a warning when they<br>provide you with general advice. You should<br>consider whether you need personal advice<br>which takes into account your individual<br>situation before you make any decisions.</p>
      <h3 class="subhead">Further advice</h3>
      <p>Depending on your relevant circumstances,<br>you may require further advice such<br>as adjustments to superannuation<br>contributions, insurance benefit amounts, or<br>a review of your strategy.<br>Further advice can generally be documented<br>in a Record of Advice and relevant file notes.<br>In some instances, a Statement of Advice<br>may be required. You may request, in writing,<br>a copy of any advice document up to seven<br>(7) years after the advice has been given.<br>An Ongoing Fee Arrangement may be<br>utilised to formalise the ongoing services<br>that your Adviser has agreed to provide for a<br>fee. Where you have entered into an ongoing<br>fee arrangement for a period of greater than<br>12 months, you will receive a Fee Disclosure</p>
    </div>

    <div class="column col-b">
      <p>Statement (FDS) annually. The FDS will<br>detail services and fees paid for the previous<br>12-month period, and the services offered<br>and estimated fees for the next 12-months.<br>To ensure the ongoing fee arrangement<br>continues, you will be required to confirm in<br>writing annually.<br>Confirmation may also include the<br>requirement to sign a Consent Form that<br>is provided to your relevant investment or<br>superannuation provider.<br>You may cease any fee arrangements or<br>disengage from your Adviser by providing<br>written notice to your Adviser or product<br>issuer.</p>
    </div>

    <div class="photo" role="img" aria-label="Photo of an adviser and client reviewing paperwork at a wooden desk"></div>

    <div class="column col-c">
      <h2 class="section-title"><span class="section-num">4</span>WHAT WE NEED FROM YOU</h2>
      <p>It’s important that you provide us with accurate<br>and complete information about your personal and<br>financial circumstances, goals and objectives so that<br>we can provide advice that is in your best interests.</p>
      <p>We also need you to inform your financial adviser<br>if there are any changes that may influence your<br>future goals or have an impact on your financial<br>plan.</p>
      <p>You have the right not to provide us with the above<br>information. However, if you do not, the advice you<br>receive may not be appropriate to your objectives,<br>financial situation and needs.</p>
      <p>We will ask you to present identification documents<br>such as passports and driver’s license, to meet our<br>obligations under the Anti-Money Laundering and<br>Counter Terrorism Finance Act to verify your identity<br>and the source of any funds.</p>
      <p>We will retain copies of this information securely.<br>You can provide instructions to us in writing, via<br>phone or via email. In some cases, we may require<br>you to provide signed instructions.</p>
      <p>At all times you are able to contact us and ask<br>questions about our advice and the products we<br>recommend.</p>
    </div>

    <div class="column col-d">
      <h2 class="section-title"><span class="section-num">5</span>MAKING A COMPLAINT</h2>
      <p>We endeavour to provide you with the<br>best advice and service at all times. If<br>you are not satisfied with our services,<br>then we encourage you to contact us.<br>You can contact us by using the details<br>below:</p>
      <p class="bold">Responsible Manager<br>Hollowbrook Financial Planning<br>PO Box 412<br>Riverton, VIC 3999<br>Email: fp@hollowbrook.com.au<br>Phone: (03) 5550 0142</p>
      <p>If you are not satisfied with our<br>response to your complaint, you may<br>lodge a complaint with the <strong>Independent</strong><br><strong>Financial Disputes Authority</strong><br><strong>(IFDA)</strong> for an independent review of<br>your matter.<br><strong>IFDA</strong> is a free and independent<br>external dispute resolution service.<br>Their details are as follows:</p>
      <p class="bold">Independent Financial Disputes<br>Authority<br>GPO Box 77, Melbourne VIC 3000<br>Email: info@ifda.org.au<br>Website: www.ifda.org.au<br>Phone: 1300 555 014</p>
    </div>

    <div class="instruction">
      <h3>How to provide instruction</h3>
      <p>Your Adviser may accept your instructions by phone, letter, text message or mail.<br>In some instances your Adviser can only accept written instructions from you, and<br>they will let you know when this is required. Your Adviser will also need to verify<br>your identity prior to acting on instructions.</p>
    </div>

    <div class="footer-label footer-label--left">FINANCIAL SERVICE GUIDE</div>
    <div class="footer-label footer-label--right">FINANCIAL SERVICE GUIDE</div>
  </section>

  <div class="page-num page-num--left">page 4</div>
  <div class="page-num page-num--right">page 5</div>
</body>
</html>
```